Design for Poster ad for Cheerleading Gym

I need someone to design a poster type ad for my Cheerleading gym. The ad will be displayed in our local mall during the holiday season. I have attached photo, but have a higher resolution available. I have also attached the spec sheet. I would like the photo with the text "Soar" over it, at the top of the ad. The background to fade from a light color (blue?) at the top to black at the bottom. Text at the bottom to be:
logo
Tumbling Classes/ Cheer Classes/ Competitive Teams
842 Velmont Rd., Torrance
ridgeflipacademy.com
phone number

Target Market(s)

Teenagers and children ages 10-18 , parents of children ages 6-10 years

Industry/Entity Type

Gym

Requirements
Must have
• The photo attached. A catch word like "Soar" at the top. The text at the bottom should include logo, Tumbling Classes/ Cheer Classes/ Competitive Teams, 842 Velmont Rd., Torrance, ridgeflipacademy.com, (424)731-2694
Nice to have
• light to dark background
Should not have
• Not a lot of text

```html
<!DOCTYPE html>
<html lang="en">
<head>
<meta charset="utf-8">
<title>Soar — Ridgeflip Academy</title>
<link rel="stylesheet" href="https://fonts.googleapis.com/css2?family=Raleway:wght@200;300;400;700&display=swap">
<style>
  :root {
    --sky-top: #2b7cc6;
    --sky-mid: #1657ae;
    --deep-blue: #0b2f7a;
    --night: #050814;
    --black: #000000;
    --white: #ffffff;
    --soft-white: #e9eef7;
    --skin-dark: #6b3a22;
    --skin-mid: #a0603a;
  }
  * { margin: 0; padding: 0; box-sizing: border-box; }
  html, body {
    width: 832px;
    height: 1200px;
    overflow: hidden;
    background: var(--black);
  }
  .poster {
    position: relative;
    width: 832px;
    height: 1200px;
    overflow: hidden;
    font-family: "Raleway", sans-serif;
    color: var(--white);
    background: linear-gradient(
      to bottom,
      var(--sky-top) 0%,
      var(--sky-mid) 30%,
      var(--deep-blue) 55%,
      var(--night) 78%,
      var(--black) 88%
    );
  }
  .headline {
    position: absolute;
    top: 160px;
    left: 0;
    width: 100%;
    display: flex;
    align-items: center;
    justify-content: center;
    gap: 22px;
  }
  .headline__rule {
    width: 88px;
    height: 2px;
    background: var(--soft-white);
  }
  .headline__word {
    display: flex;
    align-items: center;
    font-weight: 200;
    font-size: 96px;
    line-height: 1;
    letter-spacing: 4px;
    color: var(--white);
  }
  .headline__o {
    width: 76px;
    height: 76px;
    margin: 0 4px;
  }
  .athlete-photo {
    position: absolute;
    left: 270px;
    top: 340px;
    width: 300px;
    height: 580px;
    border-radius: 45% 45% 40% 40%;
    background: radial-gradient(
      ellipse at 50% 45%,
      rgba(160, 96, 58, 0.85) 0%,
      rgba(107, 58, 34, 0.7) 35%,
      rgba(20, 14, 20, 0.55) 60%,
      rgba(11, 47, 122, 0) 75%
    );
  }
  .brand {
    position: absolute;
    top: 990px;
    left: 0;
    width: 100%;
    display: flex;
    align-items: center;
    justify-content: center;
    gap: 14px;
  }
  .brand__name {
    font-weight: 300;
    font-size: 36px;
    letter-spacing: 3px;
    text-transform: uppercase;
    color: var(--white);
  }
  .brand__dot {
    width: 22px;
    height: 22px;
    border-radius: 50%;
    background: var(--white);
  }
  .services {
    position: absolute;
    top: 1090px;
    left: 0;
    width: 100%;
    text-align: center;
    font-weight: 300;
    font-size: 23px;
    color: var(--soft-white);
    letter-spacing: 0.3px;
  }
  .services__sep { margin: 0 10px; }
  .contact {
    position: absolute;
    top: 1126px;
    left: 0;
    width: 100%;
    text-align: center;
    font-weight: 300;
    font-size: 17px;
    color: var(--soft-white);
  }
  .contact__sep { margin: 0 8px; }
  .contact__strong { font-weight: 700; color: var(--white); }
</style>
</head>
<body>
  <main class="poster">
    <header class="headline">
      <span class="headline__rule"></span>
      <h1 class="headline__word" aria-label="Soar">
        <span>S</span>
        <svg class="headline__o" viewBox="0 0 76 76" aria-hidden="true">
          <circle cx="38" cy="38" r="35" fill="none" stroke="#ffffff" stroke-width="3"/>
          <circle cx="38" cy="38" r="11" fill="#ffffff"/>
        </svg>
        <span>AR</span>
      </h1>
      <span class="headline__rule"></span>
    </header>

    <div class="athlete-photo" role="img" aria-label="Photo of a cheerleader in a black outfit and white shoes performing a tucked back flip in mid-air"></div>

    <div class="brand">
      <span class="brand__name">Ridgeflip Academy</span>
      <span class="brand__dot"></span>
    </div>

    <p class="services">
      Tumbling Classes<span class="services__sep">|</span>Cheer Classes<span class="services__sep">|</span>Competitive Teams
    </p>

    <p class="contact">
      842 Velmont Rd., Torrance<span class="contact__sep">|</span><span class="contact__strong">ridgeflipacademy.com</span><span class="contact__sep contact__strong">|</span><span class="contact__strong">(424)731-2694</span>
    </p>
  </main>
</body>
</html>
```